Bag packaging design of sliced bread

The project is for design of line of sliced bread with different flavours. The brand of the bread will be "Valorina". The shape of the bread will be oval. The bread will be packed in a bag. I attach the layout of the bag. The bag will be closed with a plastic clip. I attach images of similar products. The idea is to have one main design and then each colour to be different type of bread like those in the images 2 and 5.

```html
<!DOCTYPE html>
<html lang="ro">
<head>
<meta charset="utf-8">
<title>Valorina – pâine feliată, linie de ambalaje</title>
<link rel="stylesheet" href="https://fonts.googleapis.com/css2?family=Open+Sans:wght@700&family=Oswald:wght@300;400&display=swap">
<style>
  :root {
    --backdrop: #ab9d81;
    --bread-light: #e6d3b0;
    --bread-dark: #b8946a;
    --wheat: #f2b51d;
    --text-light: #ffffff;
    --text-cream: #fbe9c8;
  }
  html, body {
    margin: 0;
    width: 1200px;
    height: 960px;
    overflow: hidden;
    background: var(--backdrop);
  }
  .range {
    position: relative;
    width: 1200px;
    height: 960px;
  }
  .bag {
    position: absolute;
    top: 80px;
    width: 300px;
    height: 800px;
  }
  .bag--seeds  { left: 80px;  --main: #5b301c; --neck: #6e3a20; --accent: #f7941d; --base: #5b301c; --tag: #f7941d; }
  .bag--rye    { left: 450px; --main: #1e7a3d; --neck: #23864a; --accent: #8dc63f; --base: #1e7a3d; --tag: #8dc63f; }
  .bag--grains { left: 820px; --main: #f26a1c; --neck: #ffc61a; --accent: #ffd21f; --base: #ffc20e; --tag: #f7a35c; }

  .bag-art { position: absolute; inset: 0; }
  .bag-neck { fill: var(--neck); }
  .bag-band { fill: var(--main); }
  .bag-base { fill: var(--base); }
  .bag-stripe { fill: none; stroke: var(--accent); stroke-width: 3; }
  .bag-ring { fill: none; stroke: var(--accent); stroke-width: 3; }
  .bag-wheat { fill: var(--wheat); }

  .bag-copy {
    position: absolute;
    left: 0;
    width: 300px;
    text-align: center;
    color: var(--text-light);
    margin: 0;
  }
  .claim {
    top: 342px;
    font: 400 14px/17px "Oswald", sans-serif;
    color: var(--text-cream);
  }
  .brand-name {
    top: 378px;
    font: 700 40px/48px "Open Sans", sans-serif;
  }
  .variety-note {
    top: 436px;
    font: 300 16px/20px "Oswald", sans-serif;
    color: var(--text-cream);
  }
  .product-name {
    top: 586px;
    font: 700 19px/23px "Open Sans", sans-serif;
  }
  .product-form {
    top: 696px;
    font: 700 19px/23px "Open Sans", sans-serif;
  }
  .weight-tag {
    top: 746px;
    left: 117px;
    width: 66px;
    padding: 3px 0;
    background: var(--tag);
    font: 700 14px/18px "Open Sans", sans-serif;
  }
</style>
</head>
<body>
<main class="range">

  <article class="bag bag--seeds">
    <svg class="bag-art" viewBox="0 0 300 800" width="300" height="800">
      <defs>
        <clipPath id="body-seeds"><path d="M60,150 H240 Q290,150 290,230 V740 Q290,790 240,790 H60 Q10,790 10,740 V230 Q10,150 60,150 Z"/></clipPath>
        <linearGradient id="bread-seeds" x1="0" y1="0" x2="1" y2="0">
          <stop offset="0" stop-color="var(--bread-dark)"/><stop offset=".5" stop-color="var(--bread-light)"/><stop offset="1" stop-color="var(--bread-dark)"/>
        </linearGradient>
      </defs>
      <path class="bag-neck" d="M15,20 Q50,5 80,22 Q115,5 150,20 Q185,5 220,22 Q250,5 285,20 L270,70 Q240,120 195,150 H105 Q60,120 30,70 Z"/>
      <g clip-path="url(#body-seeds)">
        <rect x="0" y="150" width="300" height="640" fill="url(#bread-seeds)" role="img" aria-label="Sliced seeded bread seen through the clear bag"/>
        <rect class="bag-band" x="100" y="150" width="100" height="190"/>
        <rect class="bag-band" x="0" y="330" width="300" height="160"/>
        <path class="bag-band" d="M70,490 H230 C250,560 268,620 275,700 L300,700 V800 H0 V700 L25,700 C32,620 50,560 70,490 Z"/>
        <path class="bag-stripe" d="M72,150 V330 M82,150 V330 M92,150 V330 M208,150 V330 M218,150 V330 M228,150 V330"/>
        <path class="bag-stripe" d="M58,490 C40,560 22,640 18,720 M48,490 C30,560 12,640 8,720 M242,490 C260,560 278,640 282,720 M252,490 C270,560 288,640 292,720"/>
        <path class="bag-stripe" d="M0,718 Q150,700 300,718"/>
      </g>
      <circle class="bag-ring" cx="150" cy="412" r="80"/>
      <ellipse class="bag-wheat" cx="150" cy="326" rx="44" ry="9" role="img" aria-label="Golden wheat ear decoration"/>
      <ellipse class="bag-wheat" cx="150" cy="500" rx="50" ry="10" role="img" aria-label="Golden wheat ear decoration"/>
    </svg>
    <p class="bag-copy claim">100%<br>NATURALĂ</p>
    <p class="bag-copy brand-name">Valorina</p>
    <p class="bag-copy variety-note">Cu mala de secard</p>
    <p class="bag-copy product-name">PÂINE CU<br>SEMINȚE ȘI<br>CEREALE</p>
    <p class="bag-copy product-form">feliată</p>
    <p class="bag-copy weight-tag">e500g</p>
  </article>

  <article class="bag bag--rye">
    <svg class="bag-art" viewBox="0 0 300 800" width="300" height="800">
      <defs>
        <clipPath id="body-rye"><path d="M60,150 H240 Q290,150 290,230 V740 Q290,790 240,790 H60 Q10,790 10,740 V230 Q10,150 60,150 Z"/></clipPath>
        <linearGradient id="bread-rye" x1="0" y1="0" x2="1" y2="0">
          <stop offset="0" stop-color="var(--bread-dark)"/><stop offset=".5" stop-color="var(--bread-light)"/><stop offset="1" stop-color="var(--bread-dark)"/>
        </linearGradient>
      </defs>
      <path class="bag-neck" d="M15,20 Q50,5 80,22 Q115,5 150,20 Q185,5 220,22 Q250,5 285,20 L270,70 Q240,120 195,150 H105 Q60,120 30,70 Z"/>
      <g clip-path="url(#body-rye)">
        <rect x="0" y="150" width="300" height="640" fill="url(#bread-rye)" role="img" aria-label="Sliced rye bread seen through the clear bag"/>
        <rect class="bag-band" x="100" y="150" width="100" height="190"/>
        <rect class="bag-band" x="0" y="330" width="300" height="160"/>
        <path class="bag-band" d="M70,490 H230 C250,560 268,620 275,700 L300,700 V800 H0 V700 L25,700 C32,620 50,560 70,490 Z"/>
        <path class="bag-stripe" d="M72,150 V330 M82,150 V330 M92,150 V330 M208,150 V330 M218,150 V330 M228,150 V330"/>
        <path class="bag-stripe" d="M58,490 C40,560 22,640 18,720 M48,490 C30,560 12,640 8,720 M242,490 C260,560 278,640 282,720 M252,490 C270,560 288,640 292,720"/>
        <path class="bag-stripe" d="M0,718 Q150,700 300,718"/>
      </g>
      <circle class="bag-ring" cx="150" cy="412" r="80"/>
      <ellipse class="bag-wheat" cx="150" cy="326" rx="44" ry="9" role="img" aria-label="Golden wheat ear decoration"/>
      <ellipse class="bag-wheat" cx="150" cy="500" rx="50" ry="10" role="img" aria-label="Golden wheat ear decoration"/>
    </svg>
    <p class="bag-copy claim">100%<br>NATURALĂ</p>
    <p class="bag-copy brand-name">Valorina</p>
    <p class="bag-copy variety-note">Cu mala de secard</p>
    <p class="bag-copy product-name">PÂINE CU<br>făină de<br>SECARĂ</p>
    <p class="bag-copy product-form">feliată</p>
    <p class="bag-copy weight-tag">e500g</p>
  </article>

  <article class="bag bag--grains">
    <svg class="bag-art" viewBox="0 0 300 800" width="300" height="800">
      <defs>
        <clipPath id="body-grains"><path d="M60,150 H240 Q290,150 290,230 V740 Q290,790 240,790 H60 Q10,790 10,740 V230 Q10,150 60,150 Z"/></clipPath>
        <linearGradient id="bread-grains" x1="0" y1="0" x2="1" y2="0">
          <stop offset="0" stop-color="var(--bread-dark)"/><stop offset=".5" stop-color="var(--bread-light)"/><stop offset="1" stop-color="var(--bread-dark)"/>
        </linearGradient>
      </defs>
      <path class="bag-neck" d="M15,20 Q50,5 80,22 Q115,5 150,20 Q185,5 220,22 Q250,5 285,20 L270,70 Q240,120 195,150 H105 Q60,120 30,70 Z"/>
      <g clip-path="url(#body-grains)">
        <rect x="0" y="150" width="300" height="640" fill="url(#bread-grains)" role="img" aria-label="Sliced multigrain bread seen through the clear bag"/>
        <rect class="bag-band" x="100" y="150" width="100" height="190"/>
        <rect class="bag-band" x="0" y="330" width="300" height="160"/>
        <path class="bag-band" d="M70,490 H230 C250,560 268,620 275,700 L300,700 V800 H0 V700 L25,700 C32,620 50,560 70,490 Z"/>
        <rect class="bag-base" x="0" y="712" width="300" height="90"/>
        <path class="bag-stripe" d="M72,150 V330 M82,150 V330 M92,150 V330 M208,150 V330 M218,150 V330 M228,150 V330"/>
        <path class="bag-stripe" d="M58,490 C40,560 22,640 18,720 M48,490 C30,560 12,640 8,720 M242,490 C260,560 278,640 282,720 M252,490 C270,560 288,640 292,720"/>
      </g>
      <circle class="bag-ring" cx="150" cy="412" r="80"/>
      <ellipse class="bag-wheat" cx="150" cy="326" rx="44" ry="9" role="img" aria-label="Golden wheat ear decoration"/>
      <ellipse class="bag-wheat" cx="150" cy="500" rx="50" ry="10" role="img" aria-label="Golden wheat ear decoration"/>
    </svg>
    <p class="bag-copy claim">100%<br>NATURALĂ</p>
    <p class="bag-copy brand-name">Valorina</p>
    <p class="bag-copy variety-note">Cu mala de secard</p>
    <p class="bag-copy product-name">PÂINE CU<br>SEMINȚE ȘI<br>CEREALE</p>
    <p class="bag-copy product-form">feliată</p>
    <p class="bag-copy weight-tag">e500g</p>
  </article>

</main>
</body>
</html>
```